Tidewater Ridge Podiatry

Please design a flyer using the same layout/font/colours ect as the business card (attached) please make the flyer with curved corners.
Front of DL flyer: (vertical)
Business name & logo (same as card attached)
Treatments include:
-foot, ankle & leg pain
-heel pain
-nail care
-corn & callus treatment
-bunion advice
-mechanical assessments
-orthotics
-nail surgery

Consulting within 'Bellwind Family Pharmacy' ApolloBay.
47-49 Tillbrook Parade, Corran Bay.
Call for appointments: 0411 837 260

Email:tidewaterridgepodiatry@pelmornmail.net

Reverse of flyer (horizontal)
Business name & logo

Derek Hollins
B.Pod.
B.App.Sci (HM)
NWMBQ Reg: Pod 0007384251

0422 716 308

RHS,KMB & LWF registered provider
Private Health Insurance-ancillaries cover.

```html
<!DOCTYPE html>
<html lang="en">
<head>
<meta charset="utf-8">
<title>Tidewater Ridge Podiatry – DL Flyer</title>
<link rel="stylesheet" href="https://fonts.googleapis.com/css2?family=Open+Sans:wght@400;600&display=swap">
<style>
  :root {
    --teal: #3fb8c9;
    --charcoal: #58585a;
    --ink: #3a3a3c;
    --paper: #ffffff;
    --backdrop: #ecebe8;
  }
  * { box-sizing: border-box; margin: 0; padding: 0; }
  html, body { width: 1200px; height: 828px; overflow: hidden; }
  body {
    position: relative;
    background: var(--backdrop);
    font-family: "Open Sans", Arial, sans-serif;
    color: var(--ink);
  }

  /* Front – vertical DL */
  .flyer-front {
    position: absolute; left: 82px; top: 89px;
    width: 313px; height: 662px;
    background: var(--paper);
    border-radius: 8px;
    overflow: hidden;
    box-shadow: 0 3px 10px rgba(0,0,0,.18);
  }
  .brand {
    position: absolute; left: 0; right: 0; top: 28px;
    text-align: center; color: var(--teal);
    font-weight: 400;
  }
  .brand-dot {
    display: block; width: 42px; height: 42px; margin: 0 auto 38px;
    border-radius: 50%; background: var(--teal);
  }
  .brand-name { font-size: 25px; line-height: 1.1; }
  .treatments { position: absolute; left: 30px; top: 205px; }
  .treatments h2 { font-weight: 400; font-size: 20px; color: var(--ink); margin-bottom: 10px; }
  .treatments ul { list-style: none; }
  .treatments li { font-size: 17.5px; line-height: 22.7px; color: #4a4a4c; }
  .treatments li::before { content: "» "; color: var(--teal); }
  .flyer-base { position: absolute; left: 0; bottom: 0; width: 313px; height: 215px; }
  .contact {
    position: absolute; left: 16px; right: 10px; bottom: 22px;
    color: var(--paper);
  }
  .contact .line { display: flex; align-items: center; gap: 6px; font-size: 12px; margin-bottom: 6px; }
  .contact .phone { font-size: 15px; font-weight: 600; }
  .contact .email { font-size: 12.5px; font-weight: 600; }
  .contact .venue { font-size: 10.5px; line-height: 1.4; margin-top: 16px; }

  /* Reverse – horizontal */
  .flyer-back {
    position: absolute; left: 449px; top: 440px;
    width: 666px; height: 311px;
    background: var(--paper);
    border-radius: 8px; overflow: hidden;
    box-shadow: 0 3px 10px rgba(0,0,0,.18);
  }
  .back-wave { position: absolute; left: 0; top: 0; width: 666px; height: 311px; }
  .back-brand {
    position: absolute; left: 18px; top: 92px; width: 200px;
    text-align: center; color: var(--paper); font-weight: 400;
  }
  .back-brand .brand-dot { width: 28px; height: 28px; margin-bottom: 20px; background: var(--paper); }
  .back-brand .brand-name { font-size: 18px; }
  .practitioner { position: absolute; right: 26px; top: 0; text-align: right; }
  .practitioner .name { margin-top: 42px; font-size: 17px; color: #333; letter-spacing: .3px; }
  .practitioner .quals { font-size: 12.5px; margin-top: 4px; }
  .practitioner .mobile {
    display: flex; justify-content: flex-end; align-items: center; gap: 8px;
    font-size: 19px; margin-top: 42px;
  }
  .practitioner .cover { font-size: 14.5px; line-height: 19px; margin-top: 44px; }
  .practitioner .reg { font-size: 13px; margin-top: 20px; }
</style>
</head>
<body>

<section class="flyer-front">
  <div class="brand">
    <span class="brand-dot"></span>
    <div class="brand-name">Tidewater Ridge<br>Podiatry</div>
  </div>

  <div class="treatments">
    <h2>Treatments include:</h2>
    <ul>
      <li>foot, ankle &amp; leg pain</li>
      <li>heel pain</li>
      <li>nail care</li>
      <li>corn &amp; callus treatment</li>
      <li>bunion advice</li>
      <li>mechanical assessments</li>
      <li>orthotics</li>
      <li>nail surgery</li>
    </ul>
  </div>

  <svg class="flyer-base" viewBox="0 0 280 192" preserveAspectRatio="none" aria-hidden="true">
    <path fill="var(--teal)" d="M0,14 C70,-6 210,-6 280,115 L280,192 L0,192 Z"/>
    <path fill="var(--charcoal)" d="M0,24 C60,6 130,2 168,18 C110,18 50,40 0,72 Z"/>
  </svg>

  <div class="contact">
    <div class="line">Call for appointments:
      <svg width="12" height="14" viewBox="0 0 24 24"><path fill="#fff" d="M6.6 2.5l3 3.6-1.8 2.6c1 2.4 3 4.6 5.4 5.8l2.6-1.8 3.6 3-1.6 3.3C11 18.8 4.9 12.6 3.3 4.1z"/></svg>
      <span class="phone">0411 837 260</span></div>
    <div class="line">
      <svg width="13" height="10" viewBox="0 0 26 20"><rect width="26" height="20" rx="2" fill="#fff"/><path d="M1 2l12 9 12-9" stroke="var(--teal)" stroke-width="2" fill="none"/></svg>
      <span class="email">tidewaterridgepodiatry@pelmornmail.net</span></div>
    <p class="venue">Consulting within “Bellwind Family Pharmacy” CorranBay.<br>47-49 Tillbrook Parade, Corran Bay.</p>
  </div>
</section>

<section class="flyer-back">
  <svg class="back-wave" viewBox="0 0 596 278" preserveAspectRatio="none" aria-hidden="true">
    <path fill="var(--teal)" d="M0,0 L236,0 C252,80 222,190 118,278 L0,278 Z"/>
    <path fill="#fff" d="M0,0 L231,0 C246,80 216,188 113,278 L0,278 Z"/>
    <path fill="var(--charcoal)" d="M0,0 L229,0 C242,70 228,140 204,180 C214,110 205,50 180,0 Z"/>
    <path fill="var(--teal)" d="M0,0 L180,0 C216,60 214,190 110,278 L0,278 Z"/>
  </svg>

  <div class="back-brand">
    <span class="brand-dot"></span>
    <div class="brand-name">Tidewater Ridge<br>Podiatry</div>
  </div>

  <div class="practitioner">
    <p class="name">DEREK HOLLINS</p>
    <p class="quals">B.Pod. B.App.Sci (HM)</p>
    <p class="mobile">
      <svg width="16" height="20" viewBox="0 0 24 24"><path fill="#333" d="M6.6 2.5l3 3.6-1.8 2.6c1 2.4 3 4.6 5.4 5.8l2.6-1.8 3.6 3-1.6 3.3C11 18.8 4.9 12.6 3.3 4.1z"/></svg>
      0422 716 308</p>
    <p class="cover">RHS,KMB &amp; LWF registered provider<br>Private Health Insurance-ancillaries cover.</p>
    <p class="reg">NWMBQ Reg: Pod 0007384251</p>
  </div>
</section>

</body>
</html>
```